Industrial Professional Business Card Design (Vantrel Systems)

Would like professional looking business cards. Not too busy leaning towards minimal. Should have a slogan like:
"Industrial Automation and Control".

We are a tech company that programs industrial PLC computers. We also develop custom hardware solutions. Please use the logo for inspiration.

Target Market(s)

Mining, industrial, processing, automation, factory

Industry/Entity Type

Engineering

Contact Information for Business Card

Name, phone, email, website. job title.

Font styles to use
Other font styles liked:
• droid sans

Requirements
Must have
• Use colours that go well with the logo. Not too busy design.

```html
<!DOCTYPE html>
<html lang="en">
<head>
<meta charset="utf-8">
<title>Vantrel Systems – Business Card</title>
<link rel="stylesheet" href="https://fonts.googleapis.com/css2?family=Open+Sans:wght@400;600;700&display=swap">
<style>
  :root {
    --stage: #202124;
    --front-deep: #1d4f78;
    --front-light: #1f7fac;
    --back-base: #1a4a70;
    --band-navy: #1c2c5e;
    --band-cyan: #1ea8dc;
    --band-blue: #3366bb;
    --accent: #f26b21;
    --ink: #ffffff;
  }
  * { margin: 0; padding: 0; box-sizing: border-box; }
  html, body { width: 1200px; height: 900px; overflow: hidden; }
  body {
    background: var(--stage);
    font-family: "Open Sans", "Noto Sans", sans-serif;
    color: var(--ink);
    position: relative;
  }
  .card {
    position: absolute;
    left: 270px;
    width: 660px;
    height: 377px;
    overflow: hidden;
    box-shadow: 0 10px 30px rgba(0,0,0,.5);
  }
  .card-front { top: 48px; }
  .card-back { top: 475px; background: var(--back-base); }

  .front-pattern {
    position: absolute; inset: 0;
    background:
      radial-gradient(ellipse at 75% 40%, rgba(255,255,255,.08), transparent 60%),
      linear-gradient(120deg, var(--front-deep) 0%, var(--front-light) 100%);
  }
  .brand {
    position: absolute;
    left: 0; right: 0; top: 160px;
    display: flex; align-items: center; justify-content: center; gap: 12px;
  }
  .brand-dot {
    width: 22px; height: 22px; border-radius: 50%;
    background: var(--accent);
  }
  .brand-name {
    font-size: 36px; font-weight: 400; letter-spacing: .5px;
    color: var(--ink);
  }

  .identity {
    position: absolute;
    right: 360px; top: 150px;
    text-align: right;
  }
  .person-name {
    font-size: 34px; font-weight: 700; letter-spacing: 1px; line-height: 1.1;
  }
  .person-title { font-size: 20px; font-weight: 400; margin-top: 2px; }
  .divider {
    position: absolute; left: 318px; top: 150px;
    width: 2px; height: 78px; background: var(--ink);
  }
  .contacts {
    position: absolute; left: 340px; top: 148px;
    list-style: none;
  }
  .contacts li {
    display: flex; align-items: center; gap: 10px;
    font-size: 19px; line-height: 27px;
  }
  .contacts svg { width: 18px; height: 18px; flex: none; }

  .slogan-band {
    position: absolute; left: 0; right: 0; bottom: 38px; height: 44px;
    background: linear-gradient(90deg, var(--band-navy) 0%, var(--back-base) 22%, var(--back-base) 40%, var(--band-cyan) 80%, var(--band-blue) 100%);
    display: flex; align-items: center;
  }
  .slogan {
    margin-left: 180px;
    font-size: 20px; font-weight: 400; letter-spacing: .5px;
    text-transform: uppercase;
  }
</style>
</head>
<body>
  <section class="card card-front">
    <div class="front-pattern" role="img" aria-label="Repeating faint gear-mark pattern across the card face"></div>
    <div class="brand">
      <span class="brand-dot"></span>
      <span class="brand-name">Vantrel Systems</span>
    </div>
  </section>

  <section class="card card-back">
    <div class="identity">
      <div class="person-name">MARCUS HALE</div>
      <div class="person-title">Sales Officer</div>
    </div>
    <div class="divider"></div>
    <ul class="contacts">
      <li>
        <svg viewBox="0 0 24 24"><path fill="#f26b21" d="M6.6 10.8a15 15 0 0 0 6.6 6.6l2.2-2.2c.3-.3.7-.4 1-.2 1.1.4 2.3.6 3.6.6.6 0 1 .4 1 1V20c0 .6-.4 1-1 1A17 17 0 0 1 3 4c0-.6.4-1 1-1h3.5c.6 0 1 .4 1 1 0 1.3.2 2.5.6 3.6.1.3 0 .7-.2 1z"/></svg>
        1-555-204-7710
      </li>
      <li>
        <svg viewBox="0 0 24 24"><rect x="2" y="5" width="20" height="14" fill="#f26b21"/><path d="M2 5l10 8 10-8" fill="none" stroke="#1a4a70" stroke-width="2"/></svg>
        info@vantrelsystems.com
      </li>
      <li>
        <svg viewBox="0 0 24 24" fill="none" stroke="#f26b21" stroke-width="2"><circle cx="12" cy="12" r="9"/><ellipse cx="12" cy="12" rx="4" ry="9"/><path d="M3 12h18M5 7h14M5 17h14"/></svg>
        www.vantrelsystems.com
      </li>
    </ul>
    <div class="slogan-band">
      <span class="slogan">Industrial Automation and Control</span>
    </div>
  </section>
</body>
</html>
```